Banner ad *

Replace blue banner

- An Overview / Background of the Business & Services
- We are online Wine/Spirits Merchant we ship wine throughout the USA
excluding certain states
- The Target Market / Audience you are trying to reach
- Consumers looking for online sources for hard to find wines and
vintages, our listings have detailed reviews from wine publications as long
as winery descriptions and images
- Design Specifics; any preferences or ideas for Style, Colour, Imagery,
etc
- Whichever colors will work best with wine or spirits consumers, we
have blue in our sign locally but burgundy is a rich color that is often
used with wine.

Target Market(s)

Wine drinkers ages 35-60

Industry/Entity Type

Business

Font styles to use
Serif

Colors
886aae
3176b5

Requirements
Must have
• Wine
Nice to have
• Whiskey
Should not have
• Underage people in images

```html
<!DOCTYPE html>
<html lang="en">
<head>
<meta charset="utf-8">
<title>Cellar Row – Banner</title>
<link href="https://fonts.googleapis.com/css2?family=Oswald:wght@700&family=Great+Vibes&family=Lato:wght@700;900&display=swap" rel="stylesheet">
<style>
  :root {
    --burgundy-deep: #520d26;
    --burgundy: #6a1634;
    --burgundy-soft: #7a2342;
    --wine-red: #8e1a2c;
    --amber: #b9803f;
    --leaf: #4d8a2a;
    --shelf-wood: #8a4a3a;
    --accent-blue: #2f6fa8;
    --tag-blue: #4a86b8;
    --white: #ffffff;
  }
  * { margin: 0; padding: 0; box-sizing: border-box; }
  html, body {
    width: 1200px; height: 410px; overflow: hidden;
    background: var(--burgundy-deep);
  }
  .banner {
    position: relative;
    width: 1200px; height: 410px; overflow: hidden;
    background: radial-gradient(ellipse at 55% 40%, var(--burgundy-soft) 0%, var(--burgundy) 45%, var(--burgundy-deep) 100%);
  }
  .cellar-backdrop {
    position: absolute; left: 0; top: 0; width: 300px; height: 410px;
    background: linear-gradient(90deg, rgba(60,10,26,0.55), rgba(106,22,52,0));
  }
  .shelf-photo {
    position: absolute; right: 0; top: 0; width: 340px; height: 330px;
    background: linear-gradient(90deg, rgba(106,22,52,0) 0%, rgba(138,74,58,0.45) 45%, rgba(120,58,48,0.6) 100%);
  }
  .drinks-illustration {
    position: absolute; left: 68px; top: 66px; width: 352px; height: 206px;
    border-radius: 8px;
    background:
      radial-gradient(ellipse at 30% 70%, rgba(77,138,42,0.55), rgba(77,138,42,0) 45%),
      radial-gradient(ellipse at 55% 35%, rgba(142,26,44,0.8), rgba(142,26,44,0) 40%),
      radial-gradient(ellipse at 85% 55%, rgba(185,128,63,0.75), rgba(185,128,63,0) 45%);
  }
  .brand-name {
    position: absolute; left: 478px; top: 58px;
    font-family: "Oswald", sans-serif; font-weight: 700;
    font-size: 100px; line-height: 1; letter-spacing: 1px;
    color: var(--white); text-transform: uppercase;
  }
  .divider {
    position: absolute; left: 418px; top: 178px; width: 608px; height: 3px;
    background: var(--accent-blue);
  }
  .tagline {
    position: absolute; left: 432px; top: 188px;
    font-family: "Great Vibes", cursive; font-size: 44px; line-height: 1.1;
    color: var(--white);
  }
  .shipping-note {
    position: absolute; left: 658px; top: 250px;
    display: flex; align-items: center; gap: 8px;
    font-family: "Lato", sans-serif; font-weight: 900; font-size: 25px;
    color: var(--tag-blue);
  }
  .contact-bar {
    position: absolute; left: 0; top: 338px; width: 1200px; height: 30px;
  }
  .contact-item {
    position: absolute; top: 0; height: 30px;
    display: flex; align-items: center; gap: 10px;
    font-family: "Lato", sans-serif; font-weight: 700; font-size: 17.5px;
    color: var(--white);
  }
  .contact-address { left: 142px; }
  .contact-phone { left: 560px; }
  .contact-email { left: 794px; }
  .icon { fill: var(--accent-blue); flex: none; }
</style>
</head>
<body>
  <div class="banner">
    <div class="cellar-backdrop" role="img" aria-label="Faint photo of oak wine barrels in a cellar"></div>
    <div class="shelf-photo" role="img" aria-label="Photo of wooden shelves stocked with wine bottles"></div>
    <div class="drinks-illustration" role="img" aria-label="Glass of red wine, splashing whiskey tumbler and a bunch of dark grapes with leaves"></div>

    <h1 class="brand-name">Cellar Row</h1>
    <div class="divider"></div>
    <p class="tagline">The best place to find your favourite liquor</p>

    <p class="shipping-note">
      <svg class="icon" width="24" height="24" viewBox="0 0 24 24" aria-hidden="true">
        <circle cx="11" cy="13" r="9" fill="none" stroke="#4a86b8" stroke-width="2.4"/>
        <path d="M6 12.5l4 4L22 3" fill="none" stroke="#4a86b8" stroke-width="2.6" stroke-linecap="round" stroke-linejoin="round"/>
      </svg>
      we ship throughout the USA
    </p>

    <div class="contact-bar">
      <div class="contact-item contact-address">
        <svg class="icon" width="18" height="30" viewBox="0 0 18 30" aria-hidden="true">
          <path d="M9 0C4 0 0 4 0 9c0 6.5 9 21 9 21s9-14.5 9-21C18 4 14 0 9 0zm0 13a4 4 0 1 1 0-8 4 4 0 0 1 0 8z"/>
        </svg>
        212 Harlow St - Lenox MA 01240
      </div>
      <div class="contact-item contact-phone">
        <svg class="icon" width="24" height="24" viewBox="0 0 24 24" aria-hidden="true">
          <path d="M6.6 10.8a15.1 15.1 0 0 0 6.6 6.6l2.2-2.2c.3-.3.7-.4 1-.2 1.1.4 2.3.6 3.6.6.6 0 1 .4 1 1V20c0 .6-.4 1-1 1C10.6 21 3 13.4 3 4c0-.6.4-1 1-1h3.5c.6 0 1 .4 1 1 0 1.3.2 2.5.6 3.6.1.3 0 .7-.2 1z" transform="scale(-1,1) translate(-24,0)"/>
        </svg>
        413-555-0188
      </div>
      <div class="contact-item contact-email">
        <svg class="icon" width="32" height="22" viewBox="0 0 32 22" aria-hidden="true">
          <rect x="0" y="0" width="32" height="22" rx="1.5"/>
          <path d="M1 1.5l15 11 15-11" fill="none" stroke="#6a1634" stroke-width="2"/>
        </svg>
        hello@cellarrow.com
      </div>
    </div>
  </div>
</body>
</html>
```